Business Card Design

We require a business card design for a law firm, our signature colours are maroon and cream. Our slogan is "From our family to yours", we would like the cards to be professional however feminine at the same time.

Industry/Entity Type

Business

Contact Information for Business Card

Helena Brackett & Associates Lawyers & Conveyancers, Helena Brackett LL.B. Principal Solicitor, 17 Quillon Street, Marrowdale NSW 2190

Logo styles of interest
Emblem Logo
Abstract Logo
Wordmark Logo

```html
<!DOCTYPE html>
<html lang="en">
<head>
<meta charset="utf-8">
<title>Helena Brackett &amp; Associates — Business Card</title>
<link rel="stylesheet" href="https://fonts.googleapis.com/css2?family=Tinos&family=Dancing+Script:wght@500&display=swap">
<style>
  :root {
    --maroon: #7f1812;
    --maroon-soft: #8f2a22;
    --cream: #fdf6d6;
    --serif: "Tinos", "Times New Roman", serif;
    --script: "Dancing Script", cursive;
  }
  html, body {
    margin: 0;
    padding: 0;
    overflow: hidden;
    background: var(--maroon);
  }
  .card {
    position: relative;
    width: 1200px;
    height: 726px;
    background: var(--maroon);
    color: var(--cream);
    font-family: var(--serif);
    overflow: hidden;
  }
  .emblem {
    position: absolute;
    left: 458px;
    top: 50px;
    width: 323px;
    height: 318px;
    border-radius: 14px;
    background: radial-gradient(ellipse at center, rgba(253, 246, 214, 0.22), rgba(253, 246, 214, 0.06) 70%);
  }
  .firm-name {
    position: absolute;
    left: 331px;
    width: 600px;
    top: 378px;
    margin: 0;
    text-align: center;
    font-weight: 400;
    font-size: 45px;
    line-height: 53px;
  }
  .slogan {
    position: absolute;
    left: 331px;
    width: 600px;
    top: 508px;
    margin: 0;
    text-align: center;
    font-family: var(--script);
    font-weight: 500;
    font-size: 25px;
  }
  .principal,
  .address {
    position: absolute;
    top: 560px;
    margin: 0;
    font-style: normal;
    font-size: 33px;
    line-height: 45px;
  }
  .principal { left: 64px; }
  .address { right: 67px; text-align: left; }
</style>
</head>
<body>
  <main class="card">
    <div class="emblem" role="img" aria-label="Cream scales of justice emblem with flourished scroll base"></div>

    <h1 class="firm-name">Helena Brackett &amp; Associates<br>Lawyers &amp; Conveyancers</h1>
    <p class="slogan">From our family to yours</p>

    <p class="principal">Helena Brackett LL.B.<br>Principal Solicitor</p>
    <address class="address">17 Quillon Street<br>Marrowdale NSW 2190</address>
  </main>
</body>
</html>
```